Harbor Sushi & Steak Dinner Menu

I'm looking for a MENU design with a particular feel. I want to have a base template made that I can then use for future alterations to the menu; ie I can go in and change out different entrees as the menu changes but the template will remain the same. (Ideally it would be in an Apple Pages format.). Also ideally - dinner menu will occupy 2 pages 8.5 x 11. The restaurant's name is Harbor. It is a MODERN steak house that will also feature Sushi, a Raw Bar, Exquisite Cocktails and a sophisticated nightlife crowd. I have attached our LOGO, a secondary logo that we will be featuring throughout the project including on the menu cover (the gold U). Finally - I have attached the content that we would like to see. AGAIN - I REITERATE: High end dining and lounge atmosphere. A couple of restaurants / menus that I love are Morvendel in NYC and Pellucid Steakhouse in Long Island NY. Please do not duplicate - just trying to offer some suggestions.

Requirements
Must have
• A sophisticated and elegant feel without being stuffy or old.

```html
<!DOCTYPE html>
<html lang="en">
<head>
<meta charset="utf-8">
<title>Harbor Sushi &amp; Steak — Dinner Menu</title>
<link href="https://fonts.googleapis.com/css2?family=Jost:ital,wght@0,400;0,500;1,400&display=swap" rel="stylesheet">
<style>
  :root {
    --stage: #1e1e1f;
    --page: #000000;
    --gold: #e3c878;
    --gold-deep: #c9ad5f;
    --red: #e2324f;
    --faint: #4a4426;
  }
  html, body {
    margin: 0;
    padding: 0;
    width: 1200px;
    height: 750px;
    overflow: hidden;
    background: var(--stage);
    font-family: "Jost", "Avenir", sans-serif;
  }
  .menu-spread {
    position: relative;
    width: 1200px;
    height: 750px;
  }
  .menu-page {
    position: absolute;
    top: 75px;
    width: 463px;
    height: 599px;
    background: var(--page);
    overflow: hidden;
  }
  .menu-page--sushi { left: 129px; }
  .menu-page--rolls { left: 600px; }

  .page-frame {
    position: absolute;
    left: 42px;
    top: 84px;
    width: 375px;
    height: 473px;
    border: 1.5px solid var(--gold-deep);
    z-index: 1;
  }
  .brand-name {
    position: absolute;
    left: 0;
    right: 0;
    top: 56px;
    margin: 0 auto;
    width: 118px;
    text-align: center;
    background: var(--page);
    color: var(--gold);
    font-size: 23px;
    font-weight: 500;
    letter-spacing: 4px;
    line-height: 28px;
    z-index: 2;
  }
  .section-title {
    position: absolute;
    left: 0;
    right: 0;
    top: 150px;
    margin: 0;
    text-align: center;
    color: var(--gold);
    font-size: 16px;
    font-weight: 400;
    line-height: 20px;
    letter-spacing: 0.5px;
    z-index: 2;
  }
  .corner-art {
    position: absolute;
    left: 328px;
    top: 104px;
    width: 64px;
    height: 46px;
    background: var(--gold-deep);
    border-radius: 6px;
    opacity: 0.85;
  }
  .backdrop-art {
    position: absolute;
    left: 124px;
    top: 318px;
    width: 339px;
    height: 281px;
    background: radial-gradient(ellipse at 60% 45%, rgba(74,68,38,0.8) 0%, rgba(74,68,38,0.45) 55%, rgba(74,68,38,0) 85%);
    z-index: 0;
  }
  .menu-list {
    position: absolute;
    left: 77px;
    width: 314px;
    top: 0;
    list-style: none;
    margin: 0;
    padding: 0;
    z-index: 3;
  }
  .menu-item {
    position: absolute;
    left: 0;
    width: 100%;
    color: var(--red);
  }
  .item-name {
    display: block;
    font-size: 13.5px;
    font-variant: small-caps;
    letter-spacing: 0.3px;
    line-height: 13px;
  }
  .item-line {
    display: flex;
    align-items: baseline;
    font-size: 9.5px;
    font-style: italic;
    line-height: 12px;
  }
  .item-desc { white-space: nowrap; }
  .item-leader {
    flex: 1;
    margin-left: 3px;
    border-bottom: 1.2px dotted var(--red);
    transform: translateY(-2px);
  }
</style>
</head>
<body>
<main class="menu-spread">

  <section class="menu-page menu-page--sushi">
    <div class="page-frame"></div>
    <p class="brand-name">HARBOR</p>
    <div class="corner-art" role="img" aria-label="Gold icon of two sushi rolls resting on chopsticks"></div>
    <h2 class="section-title">SUSHI SASHIMI</h2>
    <ul class="menu-list">
      <li class="menu-item" style="top:187px"><span class="item-name">Toro</span><span class="item-line"><span class="item-desc">blue fin tuna belly (gf).</span><span class="item-leader"></span></span></li>
      <li class="menu-item" style="top:221px"><span class="item-name">Unagi</span><span class="item-line"><span class="item-desc">fresh water eel (gf).</span><span class="item-leader"></span></span></li>
      <li class="menu-item" style="top:255px"><span class="item-name">Ebi</span><span class="item-line"><span class="item-desc">cooked shrimp (gf)</span><span class="item-leader"></span></span></li>
      <li class="menu-item" style="top:289px"><span class="item-name">Sake</span><span class="item-line"><span class="item-desc">salmon (gf).</span><span class="item-leader"></span></span></li>
      <li class="menu-item" style="top:323px"><span class="item-name">Hamachi</span><span class="item-line"><span class="item-desc">yellowtail (gf)</span><span class="item-leader"></span></span></li>
      <li class="menu-item" style="top:362px"><span class="item-name">Madai</span><span class="item-line"><span class="item-desc">red snapper (gf).</span><span class="item-leader"></span></span></li>
      <li class="menu-item" style="top:401px"><span class="item-name">Uni</span><span class="item-line"><span class="item-desc">sea urchin (gf)</span><span class="item-leader"></span></span></li>
      <li class="menu-item" style="top:440px"><span class="item-name">Maguro</span><span class="item-line"><span class="item-desc">tuna (gf).</span><span class="item-leader"></span></span></li>
      <li class="menu-item" style="top:480px"><span class="item-name">Hirame</span><span class="item-line"><span class="item-desc">fluke (gf).</span><span class="item-leader"></span></span></li>
    </ul>
  </section>

  <section class="menu-page menu-page--rolls">
    <div class="backdrop-art" role="img" aria-label="Large faint illustration of two sushi rolls and chopsticks"></div>
    <div class="page-frame"></div>
    <p class="brand-name">HARBOR</p>
    <h2 class="section-title">CLASSIC ROLLS</h2>
    <ul class="menu-list">
      <li class="menu-item" style="top:222px"><span class="item-name">Yellowtail</span><span class="item-line"><span class="item-desc">inside out roll with scallions (gf)</span><span class="item-leader"></span></span></li>
      <li class="menu-item" style="top:256px"><span class="item-name">Spicy Tuna or Salmon or Yellowtail</span><span class="item-line"><span class="item-desc">spicy mayo.</span><span class="item-leader"></span></span></li>
      <li class="menu-item" style="top:290px"><span class="item-name">California</span><span class="item-line"><span class="item-desc">crab meat, cucumber and avocado (gf).</span><span class="item-leader"></span></span></li>
      <li class="menu-item" style="top:324px"><span class="item-name">Vegetable</span><span class="item-line"><span class="item-desc">avocado, cucumber, asparagus and pickled reddish (gf).</span><span class="item-leader"></span></span></li>
      <li class="menu-item" style="top:358px"><span class="item-name">Spider</span><span class="item-line"><span class="item-desc">soft shell crab and avocado with eel sauce</span><span class="item-leader"></span></span></li>
      <li class="menu-item" style="top:397px"><span class="item-name">Shrimp Tempura</span><span class="item-line"><span class="item-desc">deep fried tempura shrimp and eel sauce.</span><span class="item-leader"></span></span></li>
      <li class="menu-item" style="top:436px"><span class="item-name">Alaskan</span><span class="item-line"><span class="item-desc">salmon and avocado (gf)</span><span class="item-leader"></span></span></li>
    </ul>
  </section>

</main>
</body>
</html>
```